Business Card Design Project- Removalist

I would like to surprise my husband to be with a different type of wedding present. His brother (who he owned a removalist business with) suddenly passed away from cancer recently and he has changed his business name to 'RTB' (which stands for Raising Tom Bright; but the full name doesn't need to be on the business card as it is more of a personal business name). To celebrate the new business I would like to get him some business cards made.
I would like the business name to be listed as 'RTB' and somewhere on the card I would like 'Sydney wide removals and relocation services'. I would like it to be obvious from the front of the card that it is a removalist business card. If a truck or some other feature that makes it look like a removalist business card could added it would be appreciated.
I don't mind what colours are used, but I would like the colour blue to feature somewhere in the design. It can be bright and fun, which is how Tom was.
I will also need the company's email address and phone number listed
The email address is: rtbremovals@quillpost.example
The contact number is: 0417 282 934
I don't need a contact name listed on the card, but perhaps 'Owned and operated by the Pendleworth family' could be added near the contact details in small font.
Thank you very much for considering this project!
Kind regards,
Fiona
Updates
Could you please change the mobile contact number to 0417 282 934. This is the only contact phone number required on the card now.
Thank you!

```html
<!DOCTYPE html>
<html lang="en">
<head>
<meta charset="utf-8">
<title>RTB Removals – Business Card</title>
<link href="https://fonts.googleapis.com/css2?family=Russo+One&family=Oswald:wght@500;600&family=Roboto+Condensed:wght@400;500&family=Roboto:wght@400&display=swap" rel="stylesheet">
<style>
  :root {
    --page-bg: #eef0f3;
    --card-bg: #ffffff;
    --navy: #27348b;
    --blue: #1a75bc;
    --sky: #29a9e1;
    --pale-sky: #8fd3f4;
    --fine-print: #6d6e71;
  }
  * { box-sizing: border-box; margin: 0; padding: 0; }
  html, body {
    width: 1200px;
    height: 1085px;
    overflow: hidden;
    background: var(--page-bg);
  }
  .sheet {
    position: relative;
    width: 1200px;
    height: 1085px;
  }
  .card {
    position: absolute;
    left: 200px;
    width: 800px;
    height: 480px;
    background: var(--card-bg);
    box-shadow: 0 2px 10px rgba(0, 0, 0, 0.12);
    overflow: hidden;
  }
  .card--front { top: 40px; }
  .card--back { top: 565px; }

  /* Front */
  .brand {
    position: absolute;
    top: 70px;
    left: 0;
    width: 100%;
    text-align: center;
    font-family: "Russo One", sans-serif;
    font-size: 230px;
    line-height: 1;
    color: var(--sky);
    letter-spacing: 4px;
  }
  .tagline {
    position: absolute;
    top: 355px;
    left: 0;
    width: 100%;
    text-align: center;
    font-family: "Russo One", sans-serif;
    font-size: 31px;
    color: var(--navy);
    letter-spacing: 0.5px;
    text-transform: uppercase;
  }
  .tagline__accent { color: var(--sky); }

  /* Back */
  .stripes {
    position: absolute;
    inset: 0;
    width: 800px;
    height: 480px;
  }
  .contact {
    position: absolute;
    right: 48px;
    top: 150px;
    text-align: right;
  }
  .contact__cta {
    font-family: "Oswald", sans-serif;
    font-weight: 600;
    font-size: 48px;
    line-height: 1.1;
    color: var(--navy);
  }
  .contact__phone {
    font-family: "Roboto Condensed", sans-serif;
    font-weight: 500;
    font-size: 76px;
    line-height: 1.05;
    color: var(--blue);
  }
  .contact__email {
    font-family: "Roboto Condensed", sans-serif;
    font-weight: 400;
    font-size: 36px;
    line-height: 1.2;
    color: var(--blue);
  }
  .owners {
    position: absolute;
    right: 48px;
    bottom: 36px;
    font-family: "Roboto", sans-serif;
    font-size: 17px;
    letter-spacing: 2px;
    color: var(--fine-print);
  }
</style>
</head>
<body>
<main class="sheet">
  <section class="card card--front" aria-label="Card front">
    <div class="brand">RTB</div>
    <p class="tagline">Sydney <span class="tagline__accent">wide</span> removals &amp; <span class="tagline__accent">relocation</span> services</p>
  </section>

  <section class="card card--back" aria-label="Card back">
    <svg class="stripes" viewBox="0 0 800 480" aria-hidden="true">
      <polygon points="215,0 285,0 95,480 25,480" fill="var(--blue)"/>
      <polygon points="285,0 310,0 120,480 95,480" fill="var(--pale-sky)"/>
      <polygon points="310,0 345,0 155,480 120,480" fill="var(--sky)"/>
    </svg>
    <div class="contact">
      <p class="contact__cta">CALL US TODAY!</p>
      <p class="contact__phone">0417 282 934</p>
      <p class="contact__email">rtbremovals@quillpost.example</p>
    </div>
    <p class="owners">Owned and operated by the PENDLEWORTH family</p>
  </section>
</main>
</body>
</html>
```